Lindwerk - We create living space - needs a web/WIX design

The website will be in the German language.
During the contest, I welcome designs with English text.
I will provide the German text to the winner.
We prefer WIX-Design for the future, if possible to make the website WiX-ready;

The text to be used in the webpage:
In the project description I’ve written a text about our company in English and in German – as you asked for. Please use this text in the first step.

QUALITY, EXPERTISE and EXPERIENCE
EVERYTHING UNDER A SINGLE ROOF

We are a real estate company based in Vienna, Austria. Our company's main competences are planning, conception, development, erection, sale/renting and management of properties. "We make best quality for the best price" - with this motto LINDWERK offers living space in high quality in Austria as well as in other countries. Thereby the working area of our property development focusses on both new construction and attic extensions.

QUALITÄT, KOMPETENZ UND ERFAHRUNG
ALLES UNTER EINEM DACH​

LINDWERK ist ein Komplettanbieter für Wohnimmobilien von der Vision, Konzeption, Entwicklung, Planung, Errichtung und Verkauf/Vermietung bis zur Hausverwaltung. „Wir bauen beste Qualität zum besten Preis“, unter diesem Motto bietet LINDWERK qualitativ hochwertigen, lebenswerten und nachhaltig gebauten Wohnraum sowohl in Österreich als auch in anderen Ländern an. Dabei konzentriert sich das Arbeitsfeld unserer Bauträgergesellschaft auf die beiden Kernbereiche Neubau und Dachgeschossausbau.

In the boxes “Must haves”, “Nice to haves”, “Should not haves” I’ve mentioned everything the designers need to know (font, colours etc.). AS I’ve received already some very good designs, there should be everything clear for the designers.

During the contest: homepage is welcome

Target Market(s)

Austria, Germany, Europe, Israel, USA; we would like to reach families, singles, male, female, general population and also investors

Industry/Entity Type

Real Estate Development

Number of Pages Required

5+ page

Font styles to use
Other font styles liked:
• See Upload

Colors

Designer to choose colors to be used in the design.

Requirements
Must have
• Pages called: "Company", "Projects", "Investments", "Partner", "Contact"; Link to projects; subsides (Team, News); enough space for renderings; Our company colours are yellow, grey, white and black (see our logo) - our website should be designed in this colours; Website in friendly and light colours
Nice to have
• Our company font for titles - attached; Eventually other font for the text - better readable; We prefer WIX-Design for the future, if possible to make the website WiX-ready.
• It should be clear, that the font in the attachement should be used; the provided files are pictures of our interior designs and the logo; we expect creativity from the designers, so they should use the best pictures in their opinion.
Should not have
• dark design

```html
<!DOCTYPE html>
<html lang="en">
<head>
<meta charset="utf-8">
<title>Lindwerk – We create living space</title>
<link href="https://fonts.googleapis.com/css2?family=Ubuntu:wght@400;500;700&family=Open+Sans:wght@400;600;700&display=swap" rel="stylesheet">
<style>
:root{
  --yellow:#f5e000;
  --yellow-deep:#e2cc00;
  --ink:#222222;
  --grey-dark:#3b3b3b;
  --grey-mid:#777777;
  --grey-text:#8a8a8a;
  --grey-light:#efefef;
  --line:#dddddd;
  --black:#111111;
  --white:#ffffff;
}
*{margin:0;padding:0;box-sizing:border-box}
html,body{width:1200px;height:3112px;overflow:hidden}
body{font-family:"Open Sans",Arial,sans-serif;color:var(--ink);background:var(--white);position:relative}
.heading{font-family:"Ubuntu",Arial,sans-serif}

/* top bar */
.topbar{height:32px;background:var(--grey-dark);color:#cfcfcf;font-size:11px;display:flex;align-items:center;padding:0 100px;gap:28px}
.topbar .search{margin-left:auto;width:150px;height:20px;background:#555;border-radius:2px;font-size:10px;padding:3px 8px;color:#aaa}
.topbar .dot{display:inline-block;width:8px;height:8px;background:var(--yellow);margin-right:6px;vertical-align:-1px}

/* header */
.header{height:80px;display:flex;align-items:center;padding:0 100px;border-bottom:1px solid var(--line)}
.brand{display:flex;align-items:center;gap:10px;font-family:"Ubuntu",sans-serif;font-weight:700;font-size:34px;letter-spacing:1px;color:var(--ink)}
.brand .mark{width:26px;height:26px;background:var(--yellow)}
.nav{margin-left:auto;display:flex;gap:28px;font-size:12px;font-weight:600;letter-spacing:.5px}
.nav span{color:#444}

/* hero */
.hero{position:relative;height:688px;background:linear-gradient(180deg,#d9d6cf 0%,#efece6 35%,#c9c2b6 70%,#8c8478 100%)}
.hero .photo{position:absolute;inset:0}
.hero-band{position:absolute;top:178px;left:200px;width:800px;height:92px;background:rgba(40,40,40,.72);color:var(--white);text-align:center;padding-top:16px}
.hero-band h1{font-family:"Ubuntu",sans-serif;font-size:32px;font-weight:500;letter-spacing:1px}
.hero-band p{font-size:11px;color:#ddd;margin-top:6px}
.thumbs{position:absolute;top:596px;left:200px;display:flex;gap:14px}
.thumbs div{width:122px;height:96px;border:3px solid var(--white);background:linear-gradient(135deg,#b9b3a8,#e6e2da)}
.thumbs div:nth-child(2){background:linear-gradient(135deg,#c9c4bb,#8d8a84)}
.thumbs div:nth-child(4){background:linear-gradient(135deg,#8a9aa8,#d8d8d2)}
.thumbs div:nth-child(6){background:linear-gradient(135deg,#7a8894,#cfd2d2)}
.arrow{position:absolute;top:628px;width:24px;height:32px}
.shelf{height:112px;background:linear-gradient(180deg,#9a9a9a,#e9e9e9 60%,#f4f4f4)}

/* sections */
.section-title{text-align:center;font-family:"Ubuntu",sans-serif;font-size:30px;font-weight:400;color:var(--ink)}
.rule{width:40px;height:3px;background:var(--yellow);margin:12px auto 0}
.lead{width:1000px;margin:20px auto 0;text-align:center;font-size:13px;line-height:21px;color:var(--grey-text)}
.welcome{padding-top:46px;height:320px;border-bottom:1px solid var(--line)}
.btn{display:block;width:120px;height:38px;margin:28px auto 0;background:var(--yellow);font-size:12px;font-weight:700;text-align:center;line-height:38px;color:var(--ink)}

.competences{padding-top:58px;height:688px;position:relative}
.diamonds{position:absolute;left:0;top:0;width:1200px;height:688px}
.diamonds text{font-family:"Ubuntu",sans-serif;font-size:17px;fill:var(--ink);font-weight:500}

.news{height:500px;border-top:1px solid var(--line);padding-top:40px}
.cards{display:flex;gap:48px;justify-content:center;margin-top:40px}
.card{width:304px}
.card .img{height:200px;background:linear-gradient(160deg,#c8d3dc,#9a9c98 60%,#6f7a64)}
.card:nth-child(2) .img{background:linear-gradient(160deg,#cfd9e2,#8e8c86 55%,#7b8a5e)}
.card:nth-child(3) .img{background:linear-gradient(160deg,#f2f0ec,#d7d1c6 60%,#a9a196)}
.card .date{font-size:11px;color:var(--grey-text);margin-top:14px}
.card h3{font-family:"Ubuntu",sans-serif;font-size:15px;font-weight:500;margin-top:4px}
.card p{font-size:12px;line-height:19px;color:var(--grey-text);margin-top:6px}

.partners{height:140px;background:var(--grey-light);display:flex;align-items:center;justify-content:space-between;padding:0 110px}
.partners span{font-family:"Ubuntu",sans-serif;font-size:26px;font-weight:500;color:#777;display:flex;align-items:center;gap:10px}
.partners .sq{width:18px;height:18px;background:#888}

/* footer */
.contact-band{height:388px;display:flex;margin-top:32px}
.map{width:440px;background:linear-gradient(135deg,#e9e6dc,#d8dccf 50%,#c9d4de)}
.form{width:280px;background:var(--grey-dark);padding:24px 28px;color:var(--white)}
.form h4,.reach h4{font-family:"Ubuntu",sans-serif;font-size:18px;font-weight:500;letter-spacing:1px}
.form .rule,.reach .rule{margin:8px 0 20px}
.field{height:30px;background:var(--white);margin-bottom:12px;font-size:11px;color:#999;padding:7px 10px}
.field.msg{height:74px}
.submit{width:90px;height:32px;background:var(--yellow);color:var(--ink);font-size:12px;font-weight:700;line-height:32px;text-align:center}
.reach{flex:1;background:var(--black);color:var(--white);padding:30px 40px}
.reach .brand{color:var(--white);font-size:40px}
.reach .tag{font-size:10px;letter-spacing:4px;color:#aaa;margin:4px 0 30px 36px}
.reach h4{color:var(--yellow)}
.line{display:flex;align-items:center;gap:12px;font-size:12px;color:#ccc;margin-bottom:14px}
.line svg{flex:none}
.bottom{position:absolute;left:0;top:2980px;width:1200px;height:132px;background:#2a2a2a;text-align:center;color:#bbb}
.bottom .links{display:flex;justify-content:center;gap:32px;font-size:11px;font-weight:600;padding-top:28px}
.social{display:flex;justify-content:center;gap:10px;margin-top:18px}
.social i{width:26px;height:26px;background:#555;display:block}
.copy{font-size:10px;color:#888;margin-top:14px}
</style>
</head>
<body>

<div class="topbar">
  <span><i class="dot"></i>Lindenhof 14, Vienna</span>
  <span><i class="dot"></i>+43 1 555 0192</span>
  <div class="search">Search…</div>
</div>

<header class="header">
  <div class="brand"><span class="mark"></span>LINDWERK</div>
  <nav class="nav"><span>COMPANY</span><span>PROJECTS</span><span>INVESTMENTS</span><span>PARTNER</span><span>CONTACT</span></nav>
</header>

<section class="hero">
  <div class="photo" role="img" aria-label="Bright living room interior with dining table, chairs and large windows"></div>
  <div class="hero-band">
    <h1>WE MAKE BEST QUALITY FOR THE BEST PRICE</h1>
    <p>Lindwerk offers living space in high quality in Austria as well as in other countries, focused on both</p>
    <p style="margin-top:0">new construction and attic extensions.</p>
  </div>
  <svg class="arrow" style="left:160px" viewBox="0 0 24 32"><path d="M20 2 L4 16 L20 30" fill="none" stroke="#f5e000" stroke-width="5"/></svg>
  <div class="thumbs" role="img" aria-label="Row of project preview photos">
    <div></div><div></div><div></div><div></div><div></div><div></div>
  </div>
  <svg class="arrow" style="left:1016px" viewBox="0 0 24 32"><path d="M4 2 L20 16 L4 30" fill="none" stroke="#f5e000" stroke-width="5"/></svg>
</section>
<div class="shelf"></div>

<section class="welcome">
  <h2 class="section-title">Welcome to LINDWERK</h2>
  <div class="rule"></div>
  <p class="lead">We are a real estate company based in Vienna, Austria. Our main competences are planning, conception, development, erection, sale and renting as well as the management of properties. With the motto "We make best quality for the best price" we offer living space of high quality in Austria and in other countries, focused on new construction and attic extensions for families, singles and investors alike.</p>
  <span class="btn">READ MORE</span>
</section>

<section class="competences">
  <h2 class="section-title">Our Competences</h2>
  <div class="rule"></div>
  <p class="lead">Quality, expertise and experience – everything under a single roof. From the first vision to the finished home we guide every step of the way with care, clear planning and a strong team.</p>
  <svg class="diamonds" viewBox="0 0 1200 688">
    <g fill="#efe9a0" opacity=".6">
      <polygon points="600,260 730,390 600,520 470,390"/>
    </g>
    <g fill="var(--yellow)" stroke="#fff" stroke-width="4">
      <polygon points="470,260 600,390 470,520 340,390"/>
      <polygon points="730,260 860,390 730,520 600,390"/>
      <polygon points="340,390 470,520 340,650 210,520"/>
      <polygon points="600,390 730,520 600,650 470,520"/>
      <polygon points="860,390 990,520 860,650 730,520"/>
    </g>
    <text x="470" y="396" text-anchor="middle">Development</text>
    <text x="730" y="396" text-anchor="middle">Sale/renting</text>
    <text x="340" y="526" text-anchor="middle">Conception</text>
    <text x="600" y="526" text-anchor="middle">Erection</text>
    <text x="860" y="526" text-anchor="middle">Management</text>
  </svg>
</section>

<section class="news">
  <h2 class="section-title">Latest News</h2>
  <div class="rule"></div>
  <div class="cards">
    <article class="card">
      <div class="img" role="img" aria-label="Rendering of a modern apartment building"></div>
      <div class="date">January 2015</div>
      <h3>New residence in Vienna Mitte</h3>
      <p>Our newest building offers bright flats with balconies, green courtyards and quick access to the city centre.</p>
    </article>
    <article class="card">
      <div class="img" role="img" aria-label="Rendering of a residential block with terraces"></div>
      <div class="date">January 2015</div>
      <h3>Attic extension completed</h3>
      <p>Four new roof apartments with open terraces and generous light are now ready for their future residents.</p>
    </article>
    <article class="card">
      <div class="img" role="img" aria-label="Bright furnished interior of a show apartment"></div>
      <div class="date">January 2015</div>
      <h3>Show flat opens its doors</h3>
      <p>Visit our furnished show flat and discover the quality of our interior design, materials and finishes.</p>
    </article>
  </div>
</section>

<section class="partners">
  <span>Stonefield</span>
  <span>Archeon</span>
  <span><i class="sq"></i>Corvana</span>
  <span>Meridex</span>
  <span>Brightpeak</span>
</section>

<section class="contact-band">
  <div class="map" role="img" aria-label="Street map showing the office location"></div>
  <div class="form">
    <h4>CONTACT US</h4>
    <div class="rule"></div>
    <div class="field">Name</div>
    <div class="field">Email</div>
    <div class="field">Phone</div>
    <div class="field msg">Message</div>
    <div class="submit">SUBMIT</div>
  </div>
  <div class="reach">
    <div class="brand"><span class="mark"></span>LINDWERK</div>
    <div class="tag">WE CREATE LIVING SPACE</div>
    <h4>REACH US</h4>
    <div class="rule"></div>
    <div class="line"><svg width="16" height="16" viewBox="0 0 16 16"><path d="M3 1h3l1 4-2 1a8 8 0 0 0 5 5l1-2 4 1v3a2 2 0 0 1-2 2A13 13 0 0 1 1 3a2 2 0 0 1 2-2z" fill="#f5e000"/></svg>(+43) 1 555 0192</div>
    <div class="line"><svg width="16" height="16" viewBox="0 0 16 16"><rect x="1" y="3" width="14" height="10" fill="none" stroke="#f5e000" stroke-width="1.6"/><path d="M1 3l7 6 7-6" fill="none" stroke="#f5e000" stroke-width="1.6"/></svg>office@lindwerk-example.at</div>
    <div class="line"><svg width="16" height="16" viewBox="0 0 16 16"><path d="M8 1a5 5 0 0 1 5 5c0 4-5 9-5 9S3 10 3 6a5 5 0 0 1 5-5z" fill="#f5e000"/><circle cx="8" cy="6" r="2" fill="#111"/></svg>Lindenhof 14, 1010 Vienna, Austria</div>
  </div>
</section>

<footer class="bottom">
  <div class="links"><span>COMPANY</span><span>PROJECTS</span><span>INVESTMENTS</span><span>PARTNER</span><span>CONTACT</span></div>
  <div class="social"><i></i><i></i><i></i><i></i></div>
  <div class="copy">Copyright 2015 © All Rights Reserved</div>
</footer>

</body>
</html>
```